Business Card Design

WE are looking for a premium quality Business Cards for a Law Firm . Copies of our current business card is attached.
Updates

Went on vacation/holiday

Contact Information for Business Card

xyz

```html
<!DOCTYPE html>
<html lang="en">
<head>
<meta charset="utf-8">
<title>Ashcombe Lawyers – Business Cards</title>
<link rel="stylesheet" href="https://fonts.googleapis.com/css2?family=Tinos:wght@400;700&display=swap">
<style>
  :root{
    --stage:#333333;
    --green:#0d2a1c;
    --green-deep:#0a2116;
    --green-soft:#15392a;
    --gold:#c9a45c;
    --white:#ffffff;
    --ink:#0d2a1c;
    --text:#111111;
  }
  *{box-sizing:border-box;margin:0;padding:0}
  html,body{width:1200px;height:780px;overflow:hidden}
  body{background:var(--stage);font-family:"Tinos",serif;position:relative}

  .card{position:absolute;top:230px;width:560px;height:320px;overflow:hidden;box-shadow:0 12px 30px rgba(0,0,0,.45)}

  /* Back card */
  .card--back{left:27px;background:var(--green)}
  .back-pattern{position:absolute;inset:0;background:radial-gradient(ellipse at 70% 0%,var(--green-soft) 0%,var(--green) 55%,var(--green-deep) 100%)}
  .back-brand{position:absolute;top:44px;left:0;right:0;display:flex;align-items:center;justify-content:center;gap:16px}
  .brand-circle{width:64px;height:64px;border-radius:50%;border:4px solid var(--gold);flex:none}
  .brand-name{font-weight:700;letter-spacing:.06em;line-height:1.05;text-transform:uppercase}
  .back-brand .brand-name{color:var(--white);font-size:30px}
  .back-brand .brand-name span{display:block;font-size:16px;letter-spacing:.5em}
  .tagline{position:absolute;top:160px;left:0;right:0;height:28px;background:var(--gold);color:var(--white);font-weight:700;font-size:14px;letter-spacing:.06em;text-transform:uppercase;display:flex;align-items:center;justify-content:center}
  .offices{position:absolute;top:204px;left:0;right:0;bottom:16px;display:grid;grid-template-columns:repeat(3,1fr)}
  .office{padding:0 12px 0 22px;color:var(--white);font-weight:700;font-size:11.5px;line-height:1.45;white-space:nowrap}
  .office + .office{border-left:1px solid rgba(255,255,255,.6)}
  .office-city{color:var(--gold);font-size:15px;letter-spacing:.04em;margin-bottom:3px}
  .office-phone{display:flex;align-items:center;gap:5px}
  .office-phone svg{width:11px;height:11px;fill:var(--gold)}

  /* Front card */
  .card--front{left:613px;background:var(--white)}
  .front-brand{position:absolute;left:22px;top:62px;width:190px;display:flex;flex-direction:column;align-items:center;gap:14px}
  .front-brand .brand-circle{width:96px;height:96px;border-width:5px}
  .front-brand .brand-name{color:var(--ink);font-size:27px;text-align:center}
  .front-brand .brand-name span{display:block;font-size:15px;letter-spacing:.55em;margin-top:4px}
  .divider{position:absolute;left:228px;top:34px;width:3px;height:200px;background:var(--ink)}
  .details{position:absolute;left:248px;top:24px;right:14px;color:var(--text);font-weight:700}
  .person-name{color:var(--gold);font-size:31px;letter-spacing:.02em;text-transform:uppercase;line-height:1}
  .person-role{font-size:13px;line-height:1.3;margin-top:6px}
  .person-address{font-size:13px;line-height:1.3;margin-top:12px}
  .contact-list{list-style:none;margin-top:12px;font-size:13px;line-height:1}
  .contact-list li{display:flex;align-items:center;gap:8px;height:17px}
  .contact-list svg{width:12px;height:12px;flex:none;fill:var(--gold)}
  .swoosh{position:absolute;left:0;bottom:0;width:560px;height:320px}
</style>
</head>
<body>

<section class="card card--back" aria-label="Business card back">
  <div class="back-pattern" role="img" aria-label="Repeating monogram pattern in dark green tones"></div>
  <div class="back-brand">
    <div class="brand-circle"></div>
    <div class="brand-name">Ashcombe<span>Lawyers</span></div>
  </div>
  <div class="tagline">Your Goals. Our Focus. Every Step Counts</div>
  <div class="offices">
    <div class="office">
      <div class="office-city">MELBOURNE</div>
      <div>Level 12, 140 Ellery Street</div>
      <div>MELBOURNE, VIC 3000</div>
      <div class="office-phone"><svg viewBox="0 0 24 24"><path d="M6.6 10.8a15 15 0 0 0 6.6 6.6l2.2-2.2a1 1 0 0 1 1-.25 11.4 11.4 0 0 0 3.6.57 1 1 0 0 1 1 1V20a1 1 0 0 1-1 1A17 17 0 0 1 3 4a1 1 0 0 1 1-1h3.5a1 1 0 0 1 1 1c0 1.25.2 2.45.57 3.57a1 1 0 0 1-.25 1z"/></svg>+61 03 5550 7720</div>
    </div>
    <div class="office">
      <div class="office-city">SYDNEY</div>
      <div>Level 4, Kestrel House</div>
      <div>27 Marlow Road</div>
      <div>RIVERSIDE, NSW 2199</div>
      <div class="office-phone"><svg viewBox="0 0 24 24"><path d="M6.6 10.8a15 15 0 0 0 6.6 6.6l2.2-2.2a1 1 0 0 1 1-.25 11.4 11.4 0 0 0 3.6.57 1 1 0 0 1 1 1V20a1 1 0 0 1-1 1A17 17 0 0 1 3 4a1 1 0 0 1 1-1h3.5a1 1 0 0 1 1 1c0 1.25.2 2.45.57 3.57a1 1 0 0 1-.25 1z"/></svg>+61 02 5550 1180</div>
    </div>
    <div class="office">
      <div class="office-city">PERTH</div>
      <div>Level 9, Banksia Tower</div>
      <div>62 Ridgeline Terrace</div>
      <div>PERTH, WA 6000</div>
      <div class="office-phone"><svg viewBox="0 0 24 24"><path d="M6.6 10.8a15 15 0 0 0 6.6 6.6l2.2-2.2a1 1 0 0 1 1-.25 11.4 11.4 0 0 0 3.6.57 1 1 0 0 1 1 1V20a1 1 0 0 1-1 1A17 17 0 0 1 3 4a1 1 0 0 1 1-1h3.5a1 1 0 0 1 1 1c0 1.25.2 2.45.57 3.57a1 1 0 0 1-.25 1z"/></svg>+61 08 5550 2817</div>
    </div>
  </div>
</section>

<section class="card card--front" aria-label="Business card front">
  <svg class="swoosh" viewBox="0 0 560 320" aria-hidden="true">
    <path d="M0 296 C220 288 430 258 560 222 L560 320 L0 320 Z" fill="var(--green)"/>
    <path d="M170 290 C320 276 470 246 560 206" fill="none" stroke="var(--gold)" stroke-width="3"/>
  </svg>
  <div class="front-brand">
    <div class="brand-circle"></div>
    <div class="brand-name">Ashcombe<span>Lawyers</span></div>
  </div>
  <div class="divider"></div>
  <div class="details">
    <h1 class="person-name">Marcus Hale</h1>
    <p class="person-role">Director and Principal Solicitor<br>MBA, Juris Doctor</p>
    <p class="person-address">Suite 310, Kingsford Chambers,<br>218 Ellery Street,<br>Melbourne VIC 3000</p>
    <ul class="contact-list">
      <li><svg viewBox="0 0 24 24"><path d="M6.6 10.8a15 15 0 0 0 6.6 6.6l2.2-2.2a1 1 0 0 1 1-.25 11.4 11.4 0 0 0 3.6.57 1 1 0 0 1 1 1V20a1 1 0 0 1-1 1A17 17 0 0 1 3 4a1 1 0 0 1 1-1h3.5a1 1 0 0 1 1 1c0 1.25.2 2.45.57 3.57a1 1 0 0 1-.25 1z"/></svg>+61 7 5550 1234</li>
      <li><svg viewBox="0 0 24 24"><path d="M7 1h10a2 2 0 0 1 2 2v18a2 2 0 0 1-2 2H7a2 2 0 0 1-2-2V3a2 2 0 0 1 2-2zm0 3v14h10V4zm5 15.5a1.2 1.2 0 1 0 0 2.4 1.2 1.2 0 0 0 0-2.4z"/></svg>+61 0400 555 019</li>
      <li><svg viewBox="0 0 24 24"><path d="M12 2a10 10 0 1 0 0 20 10 10 0 0 0 0-20zm6.9 6h-2.9a15 15 0 0 0-1.4-3.6A8 8 0 0 1 18.9 8zM12 4a13 13 0 0 1 1.900 4h-3.8A13 13 0 0 1 12 4zM4.3 14a8 8 0 0 1 0-4h3.4a16 16 0 0 0 0 4zm.8 2h2.9a15 15 0 0 0 1.4 3.6A8 8 0 0 1 5.1 16zM8 8H5.1a8 8 0 0 1 4.3-3.6A15 15 0 0 0 8 8zm4 12a13 13 0 0 1-1.9-4h3.8A13 13 0 0 1 12 20zm2.3-6H9.7a14 14 0 0 1 0-4h4.6a14 14 0 0 1 0 4zm.3 5.6A15 15 0 0 0 16 16h2.9a8 8 0 0 1-4.3 3.6zM16.3 14a16 16 0 0 0 0-4h3.4a8 8 0 0 1 0 4z"/></svg>www.ashcombelawyers.com.au</li>
      <li><svg viewBox="0 0 24 24"><path d="M2 5h20v14H2zm2 2v.5l8 5 8-5V7zm0 2.9V17h16V9.9l-8 5z"/></svg>marcus@ashcombelawyers.com.au</li>
    </ul>
  </div>
</section>

</body>
</html>
```